Tasman Curdworks Guild needs new business cards

We need new business cards designed and produced. We are likely to need other design work done for ads, flyers etc in future.

We would like to start with an initial business card.

The Tasman Curdworks Guild (TCG) is a membership-based not-for-profit organisation that looks after the interests of Australia's small to medium artisan cheesemakers, many of whom are also small-scale farmers. The design should be simple, using our logo, but also communicate our artisan cheese and small dairy farm focus.

The first card to be designed and produced is for me, Miriam Tolhurst. My details are:

Miriam Tolhurst
Secretary
Tasman Curdworks Guild (TCG)
http://www.curdworksguild.example
T +61452837190
E miriam.miriamtolhurst@mailbox.example

I have attached the TCG logo in jpg form. I have a higher resolution version available if needed.

Thank you!

Miriam

Miriam Tolhurst
Tasman Curdworks Guild
miriam.miriamtolhurst@mailbox.example
+61452837190

Sans Serif

• Logo (see attached file)

```html
<!DOCTYPE html>
<html lang="en">
<head>
<meta charset="utf-8">
<title>Tasman Curdworks Guild — Business Card</title>
<link rel="stylesheet" href="https://fonts.googleapis.com/css2?family=EB+Garamond:wght@400&family=Open+Sans:wght@400;600&display=swap">
<style>
  :root {
    --backdrop: #ece7e1;
    --card: #ffffff;
    --card-back: #ececec;
    --brown: #5a2e0e;
    --brown-name: #7a4a1e;
    --ink: #444444;
    --rule: #555555;
    --photo-light: #f4f4f4;
    --photo-mid: #d6d6d6;
    --photo-dark: #bdbdbd;
  }
  * { margin: 0; padding: 0; box-sizing: border-box; }
  html, body { width: 1200px; height: 1000px; overflow: hidden; }
  body { background: var(--backdrop); position: relative; font-family: "Open Sans", Arial, sans-serif; }

  .card {
    position: absolute; left: 266px; width: 666px; height: 397px;
    box-shadow: 0 3px 8px rgba(0,0,0,0.18);
    overflow: hidden;
  }
  .card--front { top: 74px; background: var(--card); }
  .card--back { top: 534px; background: var(--card-back); }

  .wordmark {
    position: absolute;
    font-family: "EB Garamond", Georgia, serif;
    font-weight: 400;
    color: var(--brown);
    line-height: 1.12;
  }
  .card--front .wordmark { left: 190px; top: 32px; font-size: 34px; }
  .card--back .wordmark { left: 158px; top: 238px; font-size: 28px; z-index: 2; }

  .holder {
    position: absolute; left: 186px; top: 234px; width: 421px;
    font-size: 17px; color: var(--brown-name); font-weight: 600;
    padding-bottom: 10px; border-bottom: 1.5px solid var(--rule);
  }
  .holder .role { font-weight: 400; color: #666; font-size: 15px; }

  .contact {
    position: absolute; left: 186px; top: 284px; width: 421px;
    color: var(--ink); font-size: 15px;
  }
  .contact-row { display: flex; align-items: center; gap: 7px; height: 24px; }
  .contact-row svg { flex: none; }
  .contact-row .gap { width: 10px; }
  .contact .site { letter-spacing: 7.4px; margin-top: 6px; font-size: 15px; }
  .contact .org { margin-top: 6px; font-size: 15px; }

  .photo {
    position: absolute; inset: 0;
    background:
      radial-gradient(ellipse 260px 170px at 450px 170px, var(--photo-light) 0%, var(--photo-mid) 70%, transparent 100%),
      linear-gradient(100deg, #e4e4e4 0%, #dcdcdc 40%, var(--photo-dark) 100%);
  }
</style>
</head>
<body>

  <section class="card card--front">
    <div class="wordmark">Tasman<br>Curdworks<br>Guild</div>

    <div class="holder">MIRIAM TOLHURST <span class="role">/ SECRETARY</span></div>

    <div class="contact">
      <div class="contact-row">
        <svg width="15" height="12" viewBox="0 0 15 12" aria-hidden="true">
          <path d="M1 4 Q7.5 -1 14 4 L12 5.5 L10 4 L5 4 L3 5.5 Z" fill="#3c2a1a"/>
          <rect x="3" y="5.5" width="9" height="6" rx="1" fill="#3c2a1a"/>
        </svg>
        <span>+61452837190</span>
        <span class="gap"></span>
        <svg width="13" height="10" viewBox="0 0 13 10" aria-hidden="true">
          <rect x="0" y="0" width="13" height="10" fill="#3c2a1a"/>
          <path d="M0 0 L6.5 5.5 L13 0" fill="none" stroke="#fff" stroke-width="1"/>
        </svg>
        <span>miriam.miriamtolhurst@mailbox.example</span>
      </div>
      <div class="site">www.curdworksguild.example</div>
      <div class="org">Tasman Curdworks Guild (TCG)</div>
    </div>
  </section>

  <section class="card card--back">
    <div class="photo" role="img" aria-label="Soft grey photograph of a hand holding a round of fresh artisan cheese"></div>
    <div class="wordmark">Tasman<br>Curdworks<br>Guild</div>
  </section>

</body>
</html>
```